Apartment Investor Business Card Design

Need a new business card designed for my multifamily investment company

Industry/Entity Type

Real Estate

Contact Information for Business Card

Garrick Pelham - President & CEO
Brightwold Holdings, LLC
4838 North 92nd Avenue, Ste 500
Omaha, NE 68999
(402) 555-0147
Garrick@brightwoldholdings.example
Www.BrightwoldHoldings.example

Colors
3176b5

```html
<!DOCTYPE html>
<html lang="en">
<head>
<meta charset="utf-8">
<title>Brightwold Holdings – Business Card</title>
<link rel="stylesheet" href="https://fonts.googleapis.com/css2?family=Cinzel:wght@500;600&family=Lato:wght@400&display=swap">
<style>
  :root {
    --backdrop: #8d532c;
    --kraft-light: #d3ae7f;
    --kraft-mid: #c49a69;
    --kraft-dark: #b58757;
    --ink: #141008;
  }
  html, body {
    margin: 0;
    padding: 0;
    width: 1200px;
    height: 900px;
    overflow: hidden;
    background: var(--backdrop);
  }
  .canvas {
    position: relative;
    width: 1200px;
    height: 900px;
  }
  .card {
    position: absolute;
    background: linear-gradient(160deg, var(--kraft-light) 0%, var(--kraft-mid) 45%, var(--kraft-dark) 100%);
    color: var(--ink);
    text-align: center;
  }
  .card--front { left: 330px; top: 90px; width: 555px; height: 343px; }
  .card--back  { left: 330px; top: 470px; width: 558px; height: 342px; }

  .line {
    position: absolute;
    left: 0;
    right: 0;
    margin: 0;
    line-height: 1;
    white-space: nowrap;
  }
  .person-name {
    top: 59px;
    font-family: "Cinzel", serif;
    font-weight: 600;
    font-size: 21px;
    letter-spacing: 0.5px;
  }
  .person-title {
    top: 85px;
    font-family: "Lato", sans-serif;
    font-size: 15px;
  }
  .contact-rule {
    position: absolute;
    top: 117px;
    left: 188px;
    width: 180px;
    height: 16px;
  }
  .contact {
    font-family: "Lato", sans-serif;
    font-size: 15.5px;
  }
  .contact--phone { top: 147px; }
  .contact--email { top: 167px; }
  .contact--web   { top: 188px; }
  .divider {
    position: absolute;
    top: 213px;
    left: 158px;
    width: 209px;
    height: 1px;
    background: var(--ink);
  }
  .company-name {
    top: 227px;
    font-family: "Cinzel", serif;
    font-weight: 600;
    font-size: 17px;
  }
  .address {
    font-family: "Lato", sans-serif;
    font-size: 15.5px;
  }
  .address--street { top: 247px; }
  .address--city   { top: 267px; }

  .brand-mark {
    position: absolute;
    left: 244px;
    top: 112px;
    width: 70px;
    height: 70px;
    background: var(--ink);
  }
  .brand-name {
    position: absolute;
    left: 0;
    right: 0;
    top: 208px;
    margin: 0;
    line-height: 1;
    font-family: "Cinzel", serif;
    font-weight: 500;
    font-size: 29px;
    letter-spacing: 0.5px;
    white-space: nowrap;
  }
</style>
</head>
<body>
<main class="canvas">

  <section class="card card--front" aria-label="Card front">
    <p class="line person-name">Garrick Pelham</p>
    <p class="line person-title">President &amp; CEO</p>

    <svg class="contact-rule" viewBox="0 0 180 16" aria-hidden="true">
      <line x1="0" y1="8" x2="52" y2="8" stroke="#141008" stroke-width="1"/>
      <line x1="127" y1="8" x2="180" y2="8" stroke="#141008" stroke-width="1"/>
      <rect x="55" y="0" width="17" height="16" rx="2" fill="#141008"/>
      <path d="M59 10 q4.5 -6 9 0 l-1 1.5 h-2 v-1.5 h-3 v1.5 h-2 z" fill="#c49a69"/>
      <rect x="80" y="0" width="17" height="16" rx="2" fill="#141008"/>
      <rect x="83" y="4" width="11" height="8" fill="none" stroke="#c49a69" stroke-width="1.2"/>
      <path d="M83 4 l5.5 4.5 l5.5 -4.5" fill="none" stroke="#c49a69" stroke-width="1.2"/>
      <rect x="105" y="0" width="17" height="16" rx="2" fill="#141008"/>
      <circle cx="113.5" cy="8" r="5" fill="none" stroke="#c49a69" stroke-width="1.2"/>
      <ellipse cx="113.5" cy="8" rx="2" ry="5" fill="none" stroke="#c49a69" stroke-width="1"/>
      <line x1="108.5" y1="8" x2="118.5" y2="8" stroke="#c49a69" stroke-width="1"/>
    </svg>

    <p class="line contact contact--phone">(402) 555-0147</p>
    <p class="line contact contact--email">Garrick@brightwoldholdings.example</p>
    <p class="line contact contact--web">www.BrightwoldHoldings.example</p>

    <div class="divider"></div>

    <p class="line company-name">Brightwold Holdings, LLC</p>
    <p class="line address address--street">4838 North 92nd Avenue, Ste 500</p>
    <p class="line address address--city">Omaha, NE 68999</p>
  </section>

  <section class="card card--back" aria-label="Card back">
    <div class="brand-mark" aria-hidden="true"></div>
    <p class="brand-name">Brightwold Holdings</p>
  </section>

</main>
</body>
</html>
```